Business Card Re-Design

Consulting Company: To build a high performance organization, you need great leaders at all levels throughout your organization. The Cedar Path Talent Institute engages, inspires, and educates current and future leaders to step beyond the ordinary and deliver exceptional results. This new breed of leaders will motivate your staff to leave the safety of complacency behind and come together to build an extraordinary organization. The current trend has been to ask our people to do more with fewer resources. People have been stepping up to the challenge, but more is required to ensure success with a new work paradigm. We work with your management team to build a successful strategy that will make your organization more effective. CPTI then supports your management team by providing a comprehensive set of proven services to empower your entire organization to successfully execute new strategies.Let CPTI help you optimize your organization’s individual and team performance today!

Target Market(s)

Federal, State and Local Government / Non profit

Industry/Entity Type

Management Consulting

Contact Information for Business Card

CPTI, inc (Cedar Path Talent Institute) Optimizing Individual and Organizational Performance

Colors
fee18a
ec1f27
474747
fbf289

Requirements
Must have
• Professional and high quality feel

```html
<!DOCTYPE html>
<html lang="en">
<head>
<meta charset="utf-8">
<title>Cedar Path Talent Institute – Business Card</title>
<link rel="stylesheet" href="https://fonts.googleapis.com/css2?family=Cormorant+SC:wght@700&family=Old+Standard+TT:wght@400;700&family=Arimo&display=swap">
<style>
  :root {
    --backdrop: #e4e4e2;
    --card: #ffffff;
    --band-red: #b80000;
    --panel-grey: #55534e;
    --gold: #e6d48a;
    --brand-brown: #3b2612;
    --mark-tan: #bdb8a4;
    --rule-white: #f4f4f4;
    --contact-text: #ffffff;
  }
  * { margin: 0; padding: 0; box-sizing: border-box; }
  html, body { width: 1189px; height: 1200px; overflow: hidden; background: var(--backdrop); }
  .canvas { position: relative; width: 1189px; height: 1200px; }

  .card {
    position: absolute; left: 140px; width: 917px; height: 524px;
    background: var(--card); overflow: hidden;
    box-shadow: 4px 6px 12px rgba(0,0,0,0.25);
  }
  .card--front { top: 45px; }
  .card--back { top: 623px; }

  .brand { position: absolute; left: 0; right: 0; text-align: center; }
  .brand__dot { display: block; margin: 0 auto; border-radius: 50%; background: var(--mark-tan); }
  .brand__name {
    font-family: "Cormorant SC", serif; font-weight: 700;
    color: var(--brand-brown); letter-spacing: 1px; line-height: 1.05;
  }
  .card--front .brand { top: 30px; }
  .card--front .brand__dot { width: 96px; height: 96px; margin-bottom: 34px; }
  .card--front .brand__name { font-size: 38px; }
  .card--back .brand { top: 66px; }
  .card--back .brand__dot { width: 150px; height: 150px; margin-bottom: 46px; }
  .card--back .brand__name { font-size: 48px; }

  .red-band { position: absolute; left: 0; right: 0; top: 285px; height: 44px; background: var(--band-red); }
  .grey-panel { position: absolute; left: 0; right: 0; top: 331px; bottom: 0; background: var(--panel-grey); }

  .person { position: absolute; left: 76px; top: 56px; color: var(--gold); font-family: "Old Standard TT", serif; font-weight: 700; }
  .person__name { font-size: 39px; line-height: 1.1; }
  .person__title { font-size: 21px; margin-top: 4px; }

  .divider { position: absolute; left: 435px; top: 20px; width: 3px; height: 152px; background: var(--rule-white); }

  .contacts { position: absolute; left: 500px; top: 22px; list-style: none; font-family: "Arimo", sans-serif; font-size: 19.5px; color: var(--contact-text); }
  .contacts li { display: flex; align-items: center; height: 31px; }
  .contacts svg { width: 15px; height: 15px; margin-right: 14px; flex: none; }

  .back-red-line { position: absolute; left: 0; right: 0; top: 465px; height: 5px; background: var(--band-red); }
  .back-grey { position: absolute; left: 0; right: 0; top: 470px; bottom: 0; background: var(--panel-grey); }
</style>
</head>
<body>
<main class="canvas">
  <section class="card card--front" aria-label="Card front">
    <div class="brand">
      <span class="brand__dot"></span>
      <p class="brand__name">Cedar Path Talent<br>Institute</p>
    </div>
    <div class="red-band"></div>
    <div class="grey-panel">
      <div class="person">
        <p class="person__name">Daniel R. Whitaker</p>
        <p class="person__title">President &amp; CEO</p>
      </div>
      <div class="divider"></div>
      <ul class="contacts">
        <li><svg viewBox="0 0 16 16"><rect width="16" height="16" rx="2" fill="#e6d48a"/><path d="M5 3l2 2-1 2 3 3 2-1 2 2-2 2C7 13 3 9 3 5z" fill="#55534e"/></svg>301-555-0142</li>
        <li><svg viewBox="0 0 16 16"><rect width="16" height="16" rx="2" fill="#e6d48a"/><rect x="3" y="6" width="10" height="7" fill="#55534e"/><rect x="4" y="3" width="8" height="3" fill="#55534e"/></svg>301-555-0178</li>
        <li><svg viewBox="0 0 16 16"><rect width="16" height="16" rx="2" fill="#e6d48a"/><rect x="3" y="5" width="10" height="7" fill="none" stroke="#55534e" stroke-width="1.4"/><path d="M3 5l5 4 5-4" fill="none" stroke="#55534e" stroke-width="1.4"/></svg>dwhitaker@cptiinc.com</li>
        <li><svg viewBox="0 0 16 16"><rect width="16" height="16" rx="2" fill="#e6d48a"/><circle cx="8" cy="8" r="5" fill="none" stroke="#55534e" stroke-width="1.4"/><path d="M3 8h10M8 3v10" stroke="#55534e" stroke-width="1.2"/></svg>www.cptiinc.com</li>
        <li><svg viewBox="0 0 16 16"><rect width="16" height="16" rx="2" fill="#e6d48a"/><path d="M8 14s-4-4.5-4-7.5a4 4 0 018 0C12 9.5 8 14 8 14z" fill="#55534e"/><circle cx="8" cy="6.5" r="1.5" fill="#e6d48a"/></svg>PO Box 4182 Fairmont, MD 20710</li>
      </ul>
    </div>
  </section>

  <section class="card card--back" aria-label="Card back">
    <div class="brand">
      <span class="brand__dot"></span>
      <p class="brand__name">Cedar Path Talent<br>Institute</p>
    </div>
    <div class="back-red-line"></div>
    <div class="back-grey"></div>
  </section>
</main>
</body>
</html>
```